Coral Ridge Builders

we are a construction company that provides the following services:
design and build new homes
building renovations
bathroom renovations
builds deck and patio
fencing and gates
retaining walls
concreting
painting
landscaping
we need a company prospectus that says who we are and the services we provide
the last page should be a quote page so we can write a quote on the spot for small jobs , so should feel that he is dealing with professional company
the front page needs to be strong and catchy that makes you want to read the rest of the pages, this will be a book form with 4 to 6 double sided pages
Target Market(s)
home owners
Industry/Entity Type
Construction
Look and feel

```html
<!DOCTYPE html>
<html lang="en">
<head>
<meta charset="utf-8">
<title>Coral Ridge Builders – Prospectus</title>
<link rel="stylesheet" href="https://fonts.googleapis.com/css2?family=Open+Sans:wght@400;600&display=swap">
<style>
:root{
  --stage:#d9d9d9;
  --ink-dark:#1b1b1b;
  --band-top:#3a3a3a;
  --paper-grey:#a9a9a9;
  --notes-band:#9a9a9a;
  --rule:#8c8c8c;
  --white:#ffffff;
  --soft-white:#e3e3e3;
}
*{margin:0;padding:0;box-sizing:border-box}
html,body{width:1200px;height:838px;overflow:hidden}
body{background:var(--stage);font-family:"Open Sans",Arial,sans-serif;display:flex;align-items:center;justify-content:center}
.prospectus{width:1110px;height:760px;display:flex;box-shadow:0 10px 30px rgba(0,0,0,.25)}
.panel{width:370px;height:100%;position:relative;overflow:hidden}
.panel + .panel{border-left:1px solid rgba(0,0,0,.3)}
.brand{display:flex;align-items:center;gap:8px;color:var(--white);font-size:13px;font-weight:600;letter-spacing:.5px}
.brand-mark{width:12px;height:12px;background:var(--white)}

/* inside panel: who we are + services */
.info{height:100%;background:linear-gradient(160deg,var(--band-top),var(--ink-dark) 70%);padding:34px 30px}
.info .brand{margin-bottom:28px}
.topic-head{display:inline-block;background:linear-gradient(#555,#222);border-radius:4px;padding:4px 18px;color:var(--white);font-size:19px;font-weight:400;margin-bottom:12px;box-shadow:0 2px 4px rgba(0,0,0,.6)}
.topic-text{color:var(--soft-white);font-size:12.5px;line-height:1.55;margin-bottom:26px}
.service-list{list-style:none;color:var(--soft-white);font-size:12.5px;line-height:1.5}
.service-list li{display:flex;align-items:center;gap:10px;padding:5px 0;border-bottom:1px solid rgba(255,255,255,.12)}
.service-list li::before{content:"";width:6px;height:6px;background:var(--white);flex:none}
.topic-close{color:var(--soft-white);font-size:12.5px;line-height:1.55;margin-top:18px}

/* quote panel */
.band{height:110px;background:linear-gradient(var(--band-top),var(--ink-dark));padding:38px 30px}
.quote{position:absolute;top:110px;left:0;right:0;bottom:0;background:var(--paper-grey)}
.quote-head{background:var(--notes-band);color:var(--ink-dark);font-size:24px;font-weight:400;padding:8px 30px}
.quote-lines{padding:10px 30px}
.quote-lines span{display:block;height:34px;border-bottom:1px solid var(--rule)}

/* cover */
.photo{position:absolute;top:110px;left:0;right:0;bottom:0;background:linear-gradient(165deg,#9fb0bf 0%,#6d6a5e 35%,#4a4236 60%,#1f3b3e 100%)}
.cover-title{position:absolute;right:26px;top:450px;text-align:right;color:var(--white)}
.cover-title h1{font-size:32px;font-weight:600;line-height:1.2}
.cover-title .web{font-size:12px;color:var(--soft-white);margin-top:4px}
.contact{position:absolute;left:0;right:0;bottom:0;height:180px;background:rgba(205,218,222,.5);padding:20px 28px;color:var(--ink-dark)}
.contact h2{font-size:17px;font-weight:400;margin-bottom:8px}
.contact p{font-size:13px;font-weight:600;line-height:1.45}
.contact .sign{font-weight:400;margin-top:6px}
</style>
</head>
<body>
<main class="prospectus">
  <section class="panel panel-info">
    <div class="info">
      <div class="brand"><span class="brand-mark"></span>Coral Ridge Builders</div>
      <h3 class="topic-head">who we are</h3>
      <p class="topic-text">Coral Ridge Builders is a local construction company helping home owners plan, build and improve the homes they live in, with honest quotes and quality work.</p>
      <h3 class="topic-head">our services</h3>
      <ul class="service-list">
        <li>Design and build new homes</li>
        <li>Building and bathroom renovations</li>
        <li>Decks, patios, fencing and gates</li>
        <li>Retaining walls and concreting</li>
        <li>Painting and landscaping</li>
      </ul>
    </div>
  </section>

  <section class="panel panel-quote">
    <div class="band"><div class="brand"><span class="brand-mark"></span>Coral Ridge Builders</div></div>
    <div class="quote">
      <h3 class="quote-head">Notes</h3>
      <div class="quote-lines">
        <span></span><span></span><span></span><span></span><span></span><span></span>
        <span></span><span></span><span></span><span></span><span></span><span></span>
        <span></span><span></span><span></span>
      </div>
    </div>
  </section>

  <section class="panel panel-cover">
    <div class="band"><div class="brand"><span class="brand-mark"></span>Coral Ridge Builders</div></div>
    <div class="photo" role="img" aria-label="Photo of a lit modern two-storey home with a pool and tree at dusk"></div>
    <div class="cover-title">
      <h1>Coral Ridge Builders</h1>
      <p class="web">www.coralridgebuilders.com</p>
    </div>
    <div class="contact">
      <h2>contact us</h2>
      <p>Coral Ridge Builders Pty Ltd<br>14 Tallow Street<br>Westbrook Victoria 3190<br>telephone 1300 555 210</p>
      <p class="sign">Coral Ridge Builders</p>
    </div>
  </section>
</main>
</body>
</html>
```